New business blog needs wordpress theme

I need a unique wordpress theme for my new business oriented blog at quietharlow.net. The blog focuses on my experience as an entrepreneur and offers insights into business problems while chronicling my experience building a new company.

I would like to see a theme that looks more like a creative professional's website, not a business website. Large photos, bright colors, unique layout. I do not want stock photos of people in suits doing business type things. Also, no pictures of me - I am blogging anonymously.

The design should communicate technology and beauty - for example, I really like the feel of the landing page at www.pebblyn.net - it is beautiful to look at but also reflects the cutting edge nature of what they are doing.

Industry/Entity Type

Business

```html
<!DOCTYPE html>
<html lang="en">
<head>
<meta charset="utf-8">
<title>Quiet Harlow</title>
<link href="https://fonts.googleapis.com/css2?family=Open+Sans:wght@400;600;700&family=PT+Serif:wght@400;700&display=swap" rel="stylesheet">
<style>
:root{
  --page:#ffffff;
  --ink:#2b2b2b;
  --muted:#8a8a8a;
  --line:#e2e2e2;
  --nav:#b9b9b9;
  --nav-dark:#a6a6a6;
  --accent:#2a4ba8;
  --badge:#333333;
  --footer:#e9e9e9;
}
*{box-sizing:border-box;margin:0;padding:0}
html,body{width:683px;height:1200px;overflow:hidden;background:var(--page)}
body{font-family:"Open Sans",Arial,sans-serif;color:var(--ink);position:relative}
.site-header{position:absolute;left:28px;top:10px;width:627px;height:60px}
.site-title{font-family:"PT Serif",Georgia,serif;font-size:25px;font-weight:400;color:#333}
.site-tagline{font-size:8px;color:var(--muted);margin-top:2px}
.search{position:absolute;right:0;top:18px;display:flex}
.search-field{width:120px;height:16px;border:1px solid #cfcfcf;background:#f6f6f6}
.search-btn{width:20px;height:16px;background:var(--accent)}
.main-nav{position:absolute;left:28px;top:75px;width:627px;height:24px;background:linear-gradient(#c6c6c6,var(--nav-dark));display:flex}
.main-nav a{font-size:9px;color:#fff;text-decoration:none;padding:0 22px;line-height:24px}
.main-nav a.active{background:var(--accent)}
.hero{position:absolute;left:28px;top:105px;width:627px;height:213px;background:linear-gradient(160deg,#f4f4f4 0%,#e4e4e4 45%,#c9c9c9 100%)}
.hero-arrow{position:absolute;top:96px;width:16px;height:16px;border-radius:50%;background:rgba(140,140,140,.6)}
.hero-arrow.prev{left:8px}.hero-arrow.next{right:8px}
.posts{position:absolute;left:58px;top:340px;width:346px}
.post{position:relative;height:235px;margin-bottom:15px;border:1px solid var(--line);box-shadow:0 2px 4px rgba(0,0,0,.12);padding:6px;background:#fff}
.post-image{height:130px;width:100%}
.img-flower{background:linear-gradient(135deg,#bfe3f4,#5aa7cf 55%,#2f6e9a)}
.img-figure{background:linear-gradient(135deg,#6fc3dc,#e35a2f 60%,#b63a1d)}
.img-daisy{background:linear-gradient(180deg,#5d9ed8,#b8d6ee 45%,#5a9a35)}
.date-badge{position:absolute;left:-16px;top:92px;width:34px;height:34px;border-radius:50%;background:var(--badge);color:#fff;text-align:center;font-size:6px;line-height:1.1;padding-top:4px}
.date-badge b{display:block;font-size:12px}
.post-title{font-size:11px;font-weight:700;margin:10px 0 3px}
.post-meta{font-size:6px;color:var(--accent)}
.post-meta span{color:var(--muted)}
.post-excerpt{font-size:6.5px;color:var(--muted);line-height:1.45;margin-top:6px}
.post-actions{position:absolute;left:6px;right:6px;bottom:6px;height:12px;display:flex;gap:5px;align-items:center}
.share{width:11px;height:11px;border:1px solid #c9c9c9;border-radius:2px}
.more{margin-left:auto;width:12px;height:12px;background:var(--accent);color:#fff;font-size:8px;text-align:center;line-height:12px}
.pagination{position:absolute;left:110px;top:1120px;display:flex;gap:3px;align-items:center;font-size:6px;color:var(--muted)}
.pagination .pg{width:12px;height:11px;border:1px solid #ccc;text-align:center;line-height:10px;color:#555}
.pagination .pg.wide{width:18px}
.pagination .label{margin-right:4px}
.sidebar{position:absolute;left:470px;top:340px;width:190px}
.widget{margin-bottom:16px}
.widget-title{font-size:10px;font-weight:600;color:#333;padding-bottom:5px;border-bottom:1px solid var(--line);margin-bottom:6px}
.cat-list{list-style:none}
.cat-list li{font-size:7px;color:#555;display:flex;align-items:center;gap:6px;height:12px}
.cat-list li::before{content:"";width:7px;height:6px;background:#555}
.cat-list li.current{color:var(--accent)}
.cat-list li.current::before{background:var(--accent)}
.comment{border:1px solid var(--line);box-shadow:0 1px 2px rgba(0,0,0,.08);padding:5px 6px;margin-bottom:7px;font-size:6px;color:var(--muted);line-height:1.4}
.comment .by{text-align:right;color:#555;margin-top:2px}
.comment .by em{color:var(--accent);font-style:normal}
.mini-post{display:flex;gap:8px;margin-bottom:9px}
.mini-thumb{width:40px;height:28px;flex:none}
.mini-post h4{font-size:7px;font-weight:600;color:var(--accent)}
.mini-post p{font-size:6px;color:var(--muted);line-height:1.35}
.tweet{display:flex;gap:8px;margin-bottom:10px}
.tweet-dot{width:9px;height:9px;border-radius:50%;background:#555;flex:none;margin-top:2px}
.tweet p{font-size:6px;color:var(--muted);line-height:1.4}
.tweet a{color:var(--accent);text-decoration:none}
.site-footer{position:absolute;left:0;top:1165px;width:683px;height:35px;background:var(--footer);border-top:1px solid #d6d6d6}
.site-footer p{position:absolute;left:28px;top:13px;font-size:6px;color:var(--muted)}
.site-footer p b{color:var(--accent);font-weight:600}
.footer-social{position:absolute;right:28px;top:10px;display:flex;gap:4px}
.footer-social span{width:13px;height:13px;border-radius:50%;background:#556}
.footer-social span.blue{background:var(--accent)}
</style>
</head>
<body>
<header class="site-header">
  <h1 class="site-title">Quiet Harlow</h1>
  <p class="site-tagline">Notes on small business, best practices, articles and tips about building a company</p>
  <div class="search"><div class="search-field"></div><div class="search-btn"></div></div>
</header>

<nav class="main-nav">
  <a class="active" href="#">Home</a>
  <a href="#">Small Business</a>
  <a href="#">Technology</a>
  <a href="#">About Harlow</a>
  <a href="#">Contact</a>
</nav>

<section class="hero" role="img" aria-label="Featured photo: fountain pen resting on a stack of white paper">
  <span class="hero-arrow prev"></span><span class="hero-arrow next"></span>
</section>

<main class="posts">
  <article class="post">
    <div class="post-image img-flower" role="img" aria-label="Photo of a blue flower with a butterfly"></div>
    <div class="date-badge">Dec<b>20</b>2012</div>
    <h2 class="post-title">Comparing Direct Mail to Dealbox – By the Numbers</h2>
    <p class="post-meta">By: Admin <span>|</span> WRITTEN IN QUIET HARLOW <span>|</span> 17 comments</p>
    <p class="post-excerpt">A simple look at what each channel costs a small shop, how many new buyers it brings in, and which one still pays back after the first month. The answer may surprise you more than the offer itself.</p>
    <div class="post-actions"><span class="share"></span><span class="share"></span><span class="share"></span><span class="share"></span><span class="share"></span><span class="more">»</span></div>
  </article>
  <article class="post">
    <div class="post-image img-figure" role="img" aria-label="Illustration of a toy figure against a bright sky"></div>
    <div class="date-badge">Dec<b>20</b>2012</div>
    <h2 class="post-title">Comparing Direct Mail to Dealbox – By the Numbers</h2>
    <p class="post-meta">By: Admin <span>|</span> WRITTEN IN QUIET HARLOW <span>|</span> 17 comments</p>
    <p class="post-excerpt">A simple look at what each channel costs a small shop, how many new buyers it brings in, and which one still pays back after the first month. The answer may surprise you more than the offer itself.</p>
    <div class="post-actions"><span class="share"></span><span class="share"></span><span class="share"></span><span class="share"></span><span class="share"></span><span class="more">»</span></div>
  </article>
  <article class="post">
    <div class="post-image img-daisy" role="img" aria-label="Photo of white daisies under a blue sky"></div>
    <div class="date-badge">Dec<b>20</b>2012</div>
    <h2 class="post-title">Comparing Direct Mail to Dealbox – By the Numbers</h2>
    <p class="post-meta">By: Admin <span>|</span> WRITTEN IN QUIET HARLOW <span>|</span> 17 comments</p>
    <p class="post-excerpt">A simple look at what each channel costs a small shop, how many new buyers it brings in, and which one still pays back after the first month. The answer may surprise you more than the offer itself.</p>
    <div class="post-actions"><span class="share"></span><span class="share"></span><span class="share"></span><span class="share"></span><span class="share"></span><span class="more">»</span></div>
  </article>
</main>

<nav class="pagination">
  <span class="label">Page 3 of 10</span>
  <span class="pg wide">«</span><span class="pg">1</span><span class="pg">2</span><span class="pg">3</span><span class="pg">4</span><span class="pg">5</span><span class="pg">…</span><span class="pg">10</span><span class="pg wide">»</span>
</nav>

<aside class="sidebar">
  <section class="widget">
    <h3 class="widget-title">Blog Categories</h3>
    <ul class="cat-list">
      <li>Blog Category 1 (5)</li>
      <li>Blog Category 2 (8)</li>
      <li class="current">Blog Category 3 (9)</li>
      <li>Blog Category 4 (12)</li>
      <li>Blog Category 5 (7)</li>
      <li>Blog Category 6 (3)</li>
    </ul>
  </section>
  <section class="widget">
    <h3 class="widget-title">Latest Comments</h3>
    <div class="comment">Great breakdown of the costs, this helped me plan my next launch.<p class="by">by <em>Lena</em> on spring plans</p></div>
    <div class="comment">I tried both last year and saw much the same numbers.<p class="by">by <em>Owen</em> on quiet growth</p></div>
    <div class="comment">Would love a follow up on pricing for service firms.<p class="by">by <em>Ravi</em> on margins</p></div>
  </section>
  <section class="widget">
    <h3 class="widget-title">Latest from our Blog</h3>
    <div class="mini-post"><div class="mini-thumb img-figure" role="img" aria-label="Post thumbnail"></div><div><h4>This is a sample Post 1</h4><p>Short note on a new idea.<br>2 hours ago</p></div></div>
    <div class="mini-post"><div class="mini-thumb img-flower" role="img" aria-label="Post thumbnail"></div><div><h4>This is a sample Post 2</h4><p>Short note on a new idea.<br>5 hours ago</p></div></div>
    <div class="mini-post"><div class="mini-thumb img-daisy" role="img" aria-label="Post thumbnail"></div><div><h4>This is a sample Post 3</h4><p>Short note on a new idea.<br>1 day ago</p></div></div>
  </section>
  <section class="widget">
    <h3 class="widget-title">Latest Tweets</h3>
    <div class="tweet"><span class="tweet-dot"></span><p>Lessons from week one of running a tiny studio. <a href="#">qh.link/a1</a><br>24 minutes ago</p></div>
    <div class="tweet"><span class="tweet-dot"></span><p>New post on pricing your first product the right way. <a href="#">qh.link/b2</a><br>24 minutes ago</p></div>
    <div class="tweet"><span class="tweet-dot"></span><p>Small teams move faster, here is why I think so. <a href="#">qh.link/c3</a><br>24 minutes ago</p></div>
  </section>
</aside>

<footer class="site-footer">
  <p>© 2012 Powered by <b>Quiet Harlow</b>. All Rights Reserved.</p>
  <div class="footer-social"><span class="blue"></span><span></span></div>
</footer>
</body>
</html>
```